Independent Consultant needs jazzy website for official company launch!

I need a simple (I think), 4-6 page wordpress design for a hosted wordpress site. I have a new logo for the company (it's a puzzle piece), and business cards but no other marketing materials developed yet.

The main features of the website are Services Offered and How Clients Use Us pages and a Resources section.

Section structure:
About us
Services Offered
How Clients Use Us
Blog
Resources

Blog items
I will use keywords and comments, categories and tags.
Images will be used and should be clickable to see larger picture.

Nature of business:
-Velmot Circle, Inc. is a start-up independent management consulting firm based in the Twin Cities, MN but with affiliates in other US locations. We specialize in brain-based, research-based organization development, learning, and coaching services.
- my background: organization behavior, neuroscience, training design and delivery, change management, management coaching, facilitation

Favourite colors:
- citron green
-orange
-grey
-blues - not turqoise or teal

Updates
•Instead of creating a bunch of custom css/html, i would like the final design to be based on one of these themes (these are my favorites):
Unsleepable, Traction, INove, Parament, Emire, Coraline, Contempt, Currents, Treba, Monochrome)

Target Market(s)
business owners, executives, mid-upper level managers in private and public sector companies

Examples of sites I kind of like:
http://www.parvenko.example
Updates

                                        I am posting a scanned front and back business card to give you an idea of the style I've used so far.  Thank you!

Industry/Entity Type

Management Consulting

Requirements
Must have
• resources page must be set up like a small store - i'll want to sell books, training materials from this site

also would like to build a mailing list over time so that i can send a periodic newsletter to visitors
Should not have
• difficult updates or require me to hire someone to make simple content edits - i'd like to do that on my own

don't want a lot of 'generic' people in photos on my site - would rather have a few real photos included or some visuals of symbols or objects that relate to the work provided

like bold, modern look but not too cutesy or young looking

```html
<!DOCTYPE html>
<html lang="en">
<head>
<meta charset="utf-8">
<title>Velmot Circle, Inc. — Home</title>
<link rel="stylesheet" href="https://fonts.googleapis.com/css2?family=Source+Sans+3:wght@400;600&display=swap">
<style>
:root{
  --page-bg:#343434;
  --brand-green:#5f9440;
  --brand-green-dark:#4d7d33;
  --citron:#8db63c;
  --citron-light:#9cc24a;
  --panel:#f0f1f3;
  --card:#ffffff;
  --ink:#333333;
  --orange:#d4621a;
  --text-green:#5a9a2c;
  --rule:#a9abae;
  --bullet:#9a9a9a;
  --white:#ffffff;
}
*{margin:0;padding:0;box-sizing:border-box}
html,body{width:1200px;height:1101px;overflow:hidden}
body{background:var(--page-bg);font-family:"Source Sans 3",Arial,sans-serif;color:var(--ink);position:relative}
.brand-mark{position:absolute;left:157px;top:18px;width:128px;height:134px;background:var(--citron)}
.brand-name{position:absolute;left:290px;top:14px;font-size:46px;font-weight:400;color:var(--white);letter-spacing:.5px;line-height:1.1}
.brand-tagline{position:absolute;left:290px;top:70px;font-size:28px;color:var(--white);line-height:1.1}
.social{position:absolute;top:64px;width:33px;height:33px;border-radius:50%;background:var(--white)}
.social.one{left:1036px}.social.two{left:1078px}
.nav-accent{position:absolute;left:290px;top:115px;width:38px;height:37px;border:2px solid var(--brand-green)}
.main-nav{position:absolute;left:331px;top:116px;width:780px;height:36px;background:var(--brand-green);display:flex;list-style:none}
.main-nav li{color:var(--white);font-size:14px;text-transform:uppercase;display:flex;align-items:center;justify-content:center;border-right:1px solid var(--brand-green-dark)}
.main-nav li:last-child{border-right:0}
.main-nav li.current{background:var(--brand-green-dark)}
.slider{position:absolute;left:91px;top:172px;width:1020px;height:324px;background:var(--citron-light)}
.slide-photo{position:absolute;left:7px;top:7px;width:1005px;height:308px;border:1px solid #dcdcdc;background:linear-gradient(90deg,#c9ccd0 0%,#e6e8ea 35%,#9fb0c6 60%,#e9ebed 78%,#f1f2f3 100%)}
.slide-title{position:absolute;left:800px;top:259px;font-size:31px;color:#333}
.slide-arrow{position:absolute;top:312px}
.slide-arrow.prev{left:115px}.slide-arrow.next{left:1056px}
.content{position:absolute;left:91px;top:506px;width:1020px;height:528px;background:var(--panel)}
.section-title{position:absolute;font-size:23px;font-weight:400;color:var(--orange)}
.intro{position:absolute;left:106px;top:573px;width:700px;font-size:13.5px;line-height:21px}
.intro p{margin-bottom:6px}
.portrait{position:absolute;left:825px;top:538px;width:271px;height:169px;border:3px solid #c4c6c9;border-radius:3px;background:linear-gradient(90deg,#e9edf1 0%,#7d93ae 40%,#3d5677 55%,#e4e6e8 75%,#b8a58c 100%)}
.divider{position:absolute;left:106px;top:740px;width:990px;height:1px;background:var(--rule)}
.sub-rule{position:absolute;left:106px;top:799px;width:694px;height:1px;background:var(--rule)}
.practice-lead{position:absolute;left:106px;top:813px;width:700px;font-size:13px;line-height:21px;color:var(--text-green)}
.practice-list{position:absolute;list-style:none;font-size:13.5px}
.practice-list li,.client-list li{position:relative;padding-left:21px;height:35.5px}
.practice-list li::before,.client-list li::before{content:"";position:absolute;left:0;top:7px;width:6px;height:6px;border-radius:50%;background:var(--bullet)}
.clients{position:absolute;left:822px;top:754px;width:274px;height:243px;background:var(--card);border-radius:3px}
.client-list{position:absolute;left:28px;top:62px;width:240px;list-style:none;font-size:13.5px;line-height:17px}
.client-list li{height:31px}
.client-list li.tall{height:48px}
.client-list li::before{top:5px}
.footer{position:absolute;left:0;top:1058px;width:1200px;text-align:center;color:#e4e4e4;font-size:13px}
</style>
</head>
<body>
<header>
  <div class="brand-mark"></div>
  <div class="brand-name">Velmot Circle, Inc.</div>
  <div class="brand-tagline">Helping people and organizations thrive!</div>
  <span class="social one" role="img" aria-label="Social link"></span>
  <span class="social two" role="img" aria-label="Social link"></span>
  <div class="nav-accent"></div>
  <ul class="main-nav">
    <li class="current" style="width:95px">Home</li>
    <li style="width:118px">About Us</li>
    <li style="width:166px">Services Offered</li>
    <li style="width:186px">How Clients Use Us</li>
    <li style="width:86px">Blog</li>
    <li style="width:129px">Resources</li>
  </ul>
</header>

<section class="slider">
  <div class="slide-photo" role="img" aria-label="Photo of a business team seated around a meeting table"></div>
</section>
<div class="slide-title">Contantry Popular</div>
<svg class="slide-arrow prev" width="24" height="40" viewBox="0 0 24 40"><polyline points="20,3 4,20 20,37" fill="none" stroke="#8a8a8a" stroke-width="4"/></svg>
<svg class="slide-arrow next" width="24" height="40" viewBox="0 0 24 40"><polyline points="4,3 20,20 4,37" fill="none" stroke="#8a8a8a" stroke-width="4"/></svg>

<main>
  <div class="content"></div>
  <h1 class="section-title" style="left:106px;top:530px">Welcome to our site</h1>
  <div class="intro">
    <p>Velmot Circle, Inc. provides research-based management consulting to help your people and organization thrive!</p>
    <p>Our work is brain-based. What we do and how we do it works with the brain's natural and hard-wired tendencies. No need to spend time and money on Organization Development, Coaching, or Learning consulting that cannot point to supportive research for its impact!</p>
    <p>Our approach is personal, respectful, and collaborative.&nbsp; Our relationships with clients are very important to us; we strive to build enduring partnerships.</p>
  </div>
  <div class="portrait" role="img" aria-label="Photo of a smiling consultant in a blue suit with colleagues behind"></div>
  <div class="divider"></div>

  <h2 class="section-title" style="left:106px;top:757px">Areas of Practice</h2>
  <div class="sub-rule"></div>
  <p class="practice-lead">Marta offers 24 years of experience in human and organization development in the private and public sectors. She works with a cadre of associates that enable to her offer a full suite of services to best meet your needs.</p>
  <ul class="practice-list" style="left:107px;top:877px">
    <li>Change management</li>
    <li>Culture assessment</li>
    <li>Learning strategy, design, delivery</li>
    <li>Group and team dynamics</li>
  </ul>
  <ul class="practice-list" style="left:396px;top:877px">
    <li>Neuroscience and neuroleadership</li>
    <li>Organizational behavior</li>
    <li>Talent development</li>
    <li>Organization design</li>
  </ul>
  <ul class="practice-list" style="left:667px;top:877px">
    <li>Strategic planning</li>
    <li>Workforce planning</li>
  </ul>

  <aside class="clients">
    <h2 class="section-title" style="left:23px;top:14px;font-size:20px">Our Clients</h2>
    <ul class="client-list">
      <li>Northfield Health Mutual</li>
      <li>Brightline Communications</li>
      <li>Crestwater Beverages, USA</li>
      <li class="tall">Meadowvale Foods, subsidiary of Prairie Hollow</li>
      <li>Lakeshire Bank</li>
    </ul>
  </aside>
</main>

<footer class="footer">Copyright © 2012 www.velmotcircle.example &nbsp;&nbsp; All rights reserved.</footer>
</body>
</html>
```